Fruit and Beverage importer and distributor. F&B industry. catering mainly to touristy venues/outlet

We need a stationary design for our company in Singapore called LurenPalm. We are a major importer and distributor of fresh thailand coconuts in Singapore hence the company name. but moving forward we intend to diversify into more fruits, juices, and beverage products to sell to our existing base of customers.
mainly catering to F&B outlets at hot tourist spots such as restaurants and theme parks and hotel chains. we core product is the fresh thai coconut. on the side we are distributing a couple of read to drink beverages
we would like to see designs that are fun and refreshing. think tropical holiday theme.
ive attached our company logo and a photo of a general look and feel id like to see for our stationary.
Industry/Entity Type
Catering
Look and feel
Each slider illustrates characteristics of the customer's brand and the style your logo design should communicate.

```html
<!DOCTYPE html>
<html lang="en">
<head>
<meta charset="utf-8">
<title>LurenPalm Stationery</title>
<link rel="stylesheet" href="https://fonts.googleapis.com/css2?family=Montserrat:wght@400;600;700&display=swap">
<style>
  :root {
    --backdrop: #1d575b;
    --teal-dark: #184d52;
    --teal: #22676f;
    --brand-red: #d62839;
    --ink-navy: #23306b;
    --rule-blue: #6a7fd0;
    --paper: #ffffff;
    --lavender: #dcdcf7;
    --sky-red: #de5a4c;
    --sky-orange: #f0a04c;
    --sun-yellow: #f4cd6c;
    --sea: #1f5d63;
    --sand: #d3a88c;
  }
  * { margin: 0; padding: 0; box-sizing: border-box; }
  html, body { width: 1200px; height: 1016px; overflow: hidden; }
  body {
    background: var(--backdrop);
    font-family: "Montserrat", sans-serif;
    position: relative;
  }
  .brand-name {
    font-family: "Montserrat", sans-serif;
    font-weight: 700;
    color: var(--brand-red);
    letter-spacing: 0.02em;
    white-space: nowrap;
  }

  /* Letterhead */
  .letterhead {
    position: absolute; left: 80px; top: 86px;
    width: 416px; height: 586px;
    background: var(--paper);
    overflow: hidden;
  }
  .letterhead-header { position: absolute; left: 0; top: 0; }
  .letterhead .brand-name {
    position: absolute; left: 176px; top: 26px; font-size: 22px;
  }
  .letter-body {
    position: absolute; left: 49px; top: 158px; width: 314px;
    color: var(--ink-navy); font-size: 6.6px; line-height: 9.2px;
  }
  .letter-body p { margin-bottom: 9px; }
  .letter-signoff { margin-top: 4px; }
  .letter-signer { margin-top: 34px; }
  .letter-footer {
    position: absolute; left: 18px; right: 18px; top: 546px;
    border-top: 1px solid var(--rule-blue);
    display: flex; justify-content: space-between;
    padding-top: 12px;
    color: var(--ink-navy); font-size: 5.4px; letter-spacing: 0.03em;
  }
  .footer-item { display: flex; align-items: center; gap: 3px; }
  .footer-item svg { width: 7px; height: 7px; fill: var(--ink-navy); }

  /* Cover */
  .cover {
    position: absolute; left: 567px; top: 50px;
    width: 422px; height: 627px; overflow: hidden;
  }
  .cover .brand-name {
    position: absolute; left: 0; right: 0; top: 352px;
    text-align: center; font-size: 48px; color: var(--paper);
  }

  /* Envelopes */
  .envelope {
    position: absolute; top: 718px; height: 247px; overflow: hidden;
    background: linear-gradient(180deg, var(--paper) 0%, var(--lavender) 100%);
  }
  .envelope-front { left: 166px; width: 440px; }
  .envelope-front .brand-name {
    position: absolute; left: 29px; top: 36px; font-size: 18px;
  }
  .envelope-contact {
    position: absolute; left: 29px; top: 88px;
    font-size: 5.6px; line-height: 7px; color: #222;
    font-weight: 600;
  }
  .envelope-back { left: 678px; width: 469px; }
  .envelope-back .brand-name {
    position: absolute; left: 0; right: 0; top: 22px;
    text-align: center; font-size: 15px;
  }
  .envelope-back svg { position: absolute; left: 0; top: 0; }
</style>
</head>
<body>

<section class="letterhead">
  <svg class="letterhead-header" width="416" height="110" viewBox="0 0 416 110">
    <defs>
      <linearGradient id="headerBand" x1="0" y1="0" x2="0" y2="1">
        <stop offset="0" stop-color="#163f45"/>
        <stop offset="1" stop-color="#2a6d76"/>
      </linearGradient>
    </defs>
    <path d="M0 0H416V78C300 70 190 86 0 108Z" fill="url(#headerBand)"/>
    <path d="M0 108C190 86 300 70 416 78V84C300 78 190 92 0 110Z" fill="#5d9fb0"/>
  </svg>
  <span class="brand-name">LurenPalm</span>

  <div class="letter-body">
    <p>Thank you for choosing LurenPalm as your partner for fresh tropical produce. Every week we bring young Thai coconuts from trusted farms straight to kitchens, bars and kiosks across Singapore, chilled, trimmed and ready to serve. Our team checks each batch for sweetness, size and water content before it leaves the cold room, so your guests always get a drink worth remembering.</p>
    <p>This season we are adding new lines to our range, including fresh mango, pineapple and passion fruit, along with a small set of ready to drink juices made for busy outlets. Samples can be arranged at your venue on request.</p>
    <p>Delivery runs daily to hotels, restaurants, beach clubs and theme parks, with early morning slots for venues that open before ten. Orders placed by four in the afternoon are packed the same evening and reach you the next day. Larger events can be booked up to a month ahead, and our staff will help you plan quantities, storage and display so nothing goes to waste and every table is stocked on time.</p>
    <p>We look forward to serving you through the year ahead. If you have any questions about pricing, delivery areas or our growing drinks range, please contact our office by phone or email and a member of our team will reply within one working day.</p>
    <div class="letter-signoff">Sincerely,</div>
    <div class="letter-signer">Daniel Tan</div>
  </div>

  <footer class="letter-footer">
    <span class="footer-item">
      <svg viewBox="0 0 10 10"><circle cx="5" cy="3" r="2.3"/><path d="M1 10C1 6.5 9 6.5 9 10Z"/></svg>LURENPALM
    </span>
    <span class="footer-item">
      <svg viewBox="0 0 10 10"><path d="M5 0A3.5 3.5 0 0 1 8.5 3.5C8.5 6 5 10 5 10S1.5 6 1.5 3.5A3.5 3.5 0 0 1 5 0ZM5 2.2A1.3 1.3 0 1 0 5 4.8A1.3 1.3 0 1 0 5 2.2Z"/></svg>SINGAPORE
    </span>
    <span class="footer-item">
      <svg viewBox="0 0 10 10"><path d="M0 2H10V8H0ZM0.8 2.6L5 5.6L9.2 2.6" stroke="#fff" stroke-width="0.8"/></svg>INFO@LURENPALM.COM
    </span>
    <span class="footer-item">
      <svg viewBox="0 0 10 10"><path d="M2 0.5L4 2.8L3 4C3.8 5.6 4.6 6.4 6 7L7.2 6L9.5 8L8.3 9.5C4.5 9.3 0.7 5.5 0.5 1.7Z"/></svg>+65 6123 4580
    </span>
    <span class="footer-item">
      <svg viewBox="0 0 10 10"><circle cx="5" cy="5" r="4.3" fill="none" stroke="#23306b" stroke-width="1"/><path d="M0.7 5H9.3M5 0.7C2.8 3 2.8 7 5 9.3M5 0.7C7.2 3 7.2 7 5 9.3" fill="none" stroke="#23306b" stroke-width="0.8"/></svg>LURENPALM.COM
    </span>
  </footer>
</section>

<section class="cover">
  <svg width="422" height="627" viewBox="0 0 422 627" role="img" aria-label="Tropical sunset beach scene with sun, sea, boats, birds, palm tree and sand">
    <defs>
      <linearGradient id="coverScene" x1="0" y1="0" x2="0" y2="1">
        <stop offset="0" stop-color="var(--sky-red)"/>
        <stop offset="0.18" stop-color="var(--sky-orange)"/>
        <stop offset="0.33" stop-color="var(--sun-yellow)"/>
        <stop offset="0.38" stop-color="#2a6670"/>
        <stop offset="0.7" stop-color="var(--sea)"/>
        <stop offset="0.8" stop-color="#c9a48c"/>
        <stop offset="1" stop-color="var(--sand)"/>
      </linearGradient>
    </defs>
    <rect width="422" height="627" fill="url(#coverScene)"/>
  </svg>
  <span class="brand-name">LurenPalm</span>
</section>

<section class="envelope envelope-front">
  <span class="brand-name">LurenPalm</span>
  <div class="envelope-contact">
    www.lurenpalm.com<br>
    info@lurenpalm.com<br>
    tel. +65 6123 4580
  </div>
</section>

<section class="envelope envelope-back">
  <svg width="469" height="247" viewBox="0 0 469 247">
    <defs>
      <linearGradient id="flapBand" x1="0" y1="0" x2="0" y2="1">
        <stop offset="0" stop-color="#163f45"/>
        <stop offset="1" stop-color="var(--teal)"/>
      </linearGradient>
      <linearGradient id="faintScene" x1="0" y1="0" x2="0" y2="1">
        <stop offset="0" stop-color="#f1f1fc"/>
        <stop offset="1" stop-color="#cfd0f2"/>
      </linearGradient>
    </defs>
    <rect x="0" y="92" width="469" height="155" fill="url(#faintScene)" role="img" aria-label="Faint sunset sea scene with boats, birds and palm tree"/>
    <path d="M0 0H469V42C469 52 455 58 440 58H29C14 58 0 52 0 42Z" fill="url(#flapBand)"/>
  </svg>
  <span class="brand-name">LurenPalm</span>
</section>

</body>
</html>
```